Heavy Duty Repairs Poster

Good afternoon - I'm looking for a poster , design to set up around different areas. The Poster must consist of the following
- Heavy duty repairs
- Pictures of Semi trucks , heavy construction equipment , trailers
- Agriculture
- All north American equipment ( see attached pictures)
- Brief Descriptions in bullet point forms
CVIPS
WELDING
AIR CONDITIONING
ENGINE REBUILDS
DIAGONSTICS
FLEET MANAGMENT
TIRE REPAIR AND SALES
ELECTRICAL , HYDRALIC , POWER TRAIN SERVICE AND REPAIRS
PART SALES
FLEET MAINTINACE
DELTEING AND TUNING
AFTER MARKET INSTALLS OUTFITTING
ONSITE & OFFSITE REPAIRS
FULL RECERTIFACTION OVERHAULING
Warranty Approved

Target Market(s)

Heavy Duty Truck , Equipment , Agriculture Owners

Industry/Entity Type

Heavy Duty Repairs

Colors
EB3D1F
EC4F4E
F09395
F8D3D4
FCEDEE

Requirements
Must have
• Pictures of : Semi trucks and trailer , Construction heavy equipment , agriculture equipment
Nice to have
• Flashy and stands out

```html
<!DOCTYPE html>
<html lang="en">
<head>
<meta charset="utf-8">
<title>Heavy Duty Repairs Poster</title>
<link href="https://fonts.googleapis.com/css2?family=Anton&family=Montserrat:wght@600;700&family=Rubik+Dirt&display=swap" rel="stylesheet">
<style>
  :root {
    --red: #eb1c24;
    --red-brand: #eb3d1f;
    --ink: #1c1c1c;
    --dark: #232323;
    --black: #000000;
    --white: #ffffff;
    --yellow: #d9a91c;
  }
  * { margin: 0; padding: 0; box-sizing: border-box; }
  html, body { width: 900px; height: 1200px; overflow: hidden; background: var(--white); }
  .poster {
    position: relative; width: 900px; height: 1200px; overflow: hidden;
    background: var(--white); font-family: "Montserrat", sans-serif;
  }
  .hero-backdrop {
    position: absolute; left: 0; top: 0; width: 900px; height: 418px;
    background: linear-gradient(180deg, #2c2c2c 0%, #262626 55%, #151515 100%);
  }
  .hero-band {
    position: absolute; left: 0; top: 407px; width: 900px; height: 11px; background: var(--red);
  }
  .brand-box {
    position: absolute; left: 38px; top: 0; width: 276px; height: 258px; background: var(--black);
    display: flex; flex-direction: column; align-items: center; justify-content: center; text-align: center;
  }
  .brand-name { color: var(--white); font-weight: 600; font-size: 16px; line-height: 1.3; }
  .brand-place { color: var(--white); font-weight: 600; font-size: 13px; margin-top: 4px; }
  .headline-top {
    position: absolute; left: 342px; top: 30px; font-family: "Anton", sans-serif; white-space: nowrap;
    color: var(--white); font-size: 76px; line-height: 1; transform: scaleX(1.12); transform-origin: left;
  }
  .headline-main {
    position: absolute; left: 342px; top: 100px; font-family: "Anton", sans-serif; white-space: nowrap;
    color: var(--red); font-size: 128px; line-height: 1; transform: scaleX(1.14); transform-origin: left;
  }
  .fleet-photo {
    position: absolute; left: 232px; top: 222px; width: 668px; height: 222px;
    background: linear-gradient(90deg, #8a7530 0%, #d4a524 25%, #6d6a66 45%, #e0b321 70%, #3a3a3a 100%);
    clip-path: polygon(4% 100%, 10% 60%, 30% 30%, 50% 10%, 80% 0, 100% 20%, 100% 100%);
  }
  .services-title {
    position: absolute; left: 38px; top: 500px; font-family: "Rubik Dirt", sans-serif; font-size: 40px; line-height: 1;
  }
  .services-title .dark { color: var(--ink); }
  .services-title .accent { color: var(--red); }
  .services-rule { position: absolute; left: 38px; top: 547px; width: 180px; height: 2px; background: var(--ink); }
  .service-list { position: absolute; left: 38px; top: 570px; list-style: none; }
  .service-list li {
    position: relative; padding-left: 34px; height: 30.2px; line-height: 20px;
    font-weight: 700; font-size: 15.5px; color: var(--ink); letter-spacing: 0.2px;
  }
  .service-list li::before {
    content: ""; position: absolute; left: 0; top: 3px;
    border-left: 13px solid var(--red); border-top: 7px solid transparent; border-bottom: 7px solid transparent;
  }
  .gallery-frame {
    position: absolute; left: 572px; top: 466px; width: 290px; height: 648px; background: var(--white);
  }
  .gallery-column {
    position: absolute; left: 582px; top: 473px; width: 270px; height: 629px; background: var(--ink);
  }
  .gallery-shot {
    position: absolute; left: 486px; width: 296px; border: 9px solid var(--white);
  }
  .gallery-shot.welding { top: 501px; height: 162px; background: linear-gradient(135deg, #3d3a30, #1b1b1b 60%, #5b4b32); }
  .gallery-shot.engine { top: 673px; height: 162px; background: linear-gradient(135deg, #6a6460, #242424 55%, #4e4a46); }
  .gallery-shot.parts { top: 847px; height: 162px; background: linear-gradient(135deg, #dcdcdc, #8a8680 50%, #3a3030); }
  .footer {
    position: absolute; left: 0; top: 1057px; width: 900px; height: 143px; background: var(--dark);
  }
  .gallery-frame, .gallery-column, .gallery-shot { z-index: 2; }
  .warranty-tag {
    position: absolute; left: 286px; top: 1041px; width: 286px; height: 34px; z-index: 3;
    background: var(--red); clip-path: polygon(5% 0, 100% 0, 100% 100%, 0 100%);
    color: var(--white); font-weight: 700; font-size: 17px; line-height: 34px; text-align: right; padding-right: 22px;
  }
  .phone-icon { position: absolute; left: 38px; top: 1101px; width: 48px; height: 74px; z-index: 3; }
  .call-label {
    position: absolute; left: 95px; top: 1098px; color: var(--red); font-weight: 700; font-size: 17.5px; z-index: 3;
  }
  .call-number {
    position: absolute; left: 94px; top: 1118px; color: var(--white); font-family: "Rubik Dirt", sans-serif; white-space: nowrap;
    font-size: 62px; line-height: 1; letter-spacing: 1px; z-index: 3; transform: scaleX(0.84); transform-origin: left;
  }
  .web {
    position: absolute; left: 574px; top: 1156px; display: flex; align-items: center; gap: 12px; z-index: 3;
    color: var(--white); font-weight: 700; font-size: 17px; letter-spacing: 3.2px;
  }
  .web-globe { width: 12px; height: 12px; }
</style>
</head>
<body>
<main class="poster">
  <div class="hero-backdrop" role="img" aria-label="Dim industrial site with crane and plant silhouettes"></div>
  <div class="hero-band"></div>

  <div class="brand-box">
    <p class="brand-name">Ridgeline Mechanical Services</p>
    <p class="brand-place">Ashford Creek , Alberta</p>
  </div>

  <h1>
    <span class="headline-top">HEAVY DUTY</span>
    <span class="headline-main">REPAIRS</span>
  </h1>

  <div class="fleet-photo" role="img" aria-label="Yellow wheel loaders and a weathered semi truck lined up side by side"></div>

  <h2 class="services-title"><span class="dark">OUR</span> <span class="accent">SERVICES</span></h2>
  <div class="services-rule"></div>
  <ul class="service-list">
    <li>CVIPS</li>
    <li>WELDING</li>
    <li>AIR CONDITIONING</li>
    <li>ENGINE REBUILDS</li>
    <li>DIAGONSTICS</li>
    <li>FLEET MANAGMENT</li>
    <li>TIRE REPAIR AND SALES</li>
    <li>ELECTRICAL , HYDRALIC , POWER TRAIN</li>
    <li>SERVICE AND REPAIRS</li>
    <li>PART SALES</li>
    <li>FLEET MAINTINACE</li>
    <li>DELTEING AND TUNING</li>
    <li>AFTER MARKET INSTALLS OUTFITTING</li>
    <li>ONSITE &amp; OFFSITE REPAIRS</li>
    <li>FULL RECERTIFACTION OVERHAULING</li>
  </ul>

  <div class="footer"></div>

  <div class="gallery-frame"></div>
  <div class="gallery-column"></div>
  <div class="gallery-shot welding" role="img" aria-label="Mechanic grinding metal with sparks in a workshop"></div>
  <div class="gallery-shot engine" role="img" aria-label="Hands working on an engine bay with a screwdriver"></div>
  <div class="gallery-shot parts" role="img" aria-label="Carburetor and tools laid out on a cloth"></div>

  <div class="warranty-tag">WARRANTY APPROVED</div>

  <svg class="phone-icon" viewBox="0 0 48 74" aria-hidden="true">
    <rect x="2.5" y="2.5" width="43" height="69" rx="6" fill="none" stroke="#fff" stroke-width="5"/>
    <line x1="18" y1="9" x2="30" y2="9" stroke="#fff" stroke-width="2.5" stroke-linecap="round"/>
    <rect x="8" y="14" width="32" height="44" fill="none" stroke="#fff" stroke-width="2"/>
    <circle cx="24" cy="65" r="3" fill="#fff"/>
  </svg>
  <p class="call-label">CALL FOR MORE DETAILS</p>
  <p class="call-number">780 555 0142</p>

  <p class="web">
    <svg class="web-globe" viewBox="0 0 12 12" aria-hidden="true">
      <circle cx="6" cy="6" r="5.5" fill="#eb1c24"/>
      <path d="M0.5 6h11M6 0.5v11" stroke="#232323" stroke-width="1"/>
    </svg>
    WWW.WEBSITE.COM
  </p>
</main>
</body>
</html>
```